Album Cover Art for New Single

Independent singer-songwriter and pianist, seeking design work for a new single "Walk Along the Harbor". Christian & Gospel music format. See attached for master recording.

This single is personal for me, so I'm looking for an image that really captures the heart of the message. Redemption, forgiveness, prodigals returning home to a loving father.
Updates

Target Market(s)

Millenials

Colors

Designer to choose colors to be used in the design.

Requirements
Must have
• simple graphic, must include the following text:
• Walk Along the Harbor
• Dale Fennimore
Should not have
• Avoid "cheesy" look and feel.

```html
<!DOCTYPE html>
<html lang="en">
<head>
<meta charset="utf-8">
<title>Walk Along the Harbor — Dale Fennimore</title>
<link rel="stylesheet" href="https://fonts.googleapis.com/css2?family=Montserrat:wght@200;600&family=Playfair+Display:wght@600&display=swap">
<style>
  :root {
    --sky-top: #c6cccb;
    --sky-mid: #cdd8d7;
    --sky-bottom: #cfe4e3;
    --cloud-pink: #e0a3a6;
    --cloud-rose: #d98d93;
    --cloud-light: #f1d9d8;
    --title-white: #ffffff;
    --artist-white: #fdf7f6;
  }
  * { margin: 0; padding: 0; box-sizing: border-box; }
  html, body {
    width: 1200px;
    height: 1200px;
    overflow: hidden;
    background: var(--sky-mid);
  }
  .cover {
    position: relative;
    width: 1200px;
    height: 1200px;
    overflow: hidden;
  }
  .sky-photo {
    position: absolute;
    inset: 0;
    background:
      radial-gradient(ellipse 520px 210px at 560px 600px, var(--cloud-rose) 0%, rgba(217,141,147,0.55) 45%, rgba(217,141,147,0) 100%),
      radial-gradient(ellipse 640px 300px at 520px 520px, var(--cloud-light) 0%, rgba(241,217,216,0.6) 40%, rgba(241,217,216,0) 100%),
      radial-gradient(ellipse 780px 360px at 600px 640px, rgba(224,163,166,0.55) 0%, rgba(224,163,166,0) 100%),
      linear-gradient(180deg, var(--sky-top) 0%, var(--sky-mid) 55%, var(--sky-bottom) 100%);
  }
  .title {
    position: absolute;
    top: 214px;
    left: 0;
    width: 100%;
    text-align: center;
    font-family: "Montserrat", sans-serif;
    font-size: 180px;
    line-height: 172px;
    color: var(--title-white);
    text-transform: uppercase;
  }
  .title-line { display: block; font-weight: 200; }
  .title-line--lead { font-weight: 600; }
  .artist {
    position: absolute;
    top: 1040px;
    left: 0;
    width: 100%;
    text-align: center;
    font-family: "Playfair Display", serif;
    font-weight: 600;
    font-size: 28px;
    letter-spacing: 0.55em;
    padding-left: 0.55em;
    color: var(--artist-white);
    text-transform: uppercase;
  }
</style>
</head>
<body>
  <main class="cover">
    <div class="sky-photo" role="img" aria-label="Photograph of a soft pink cloud drifting across a pale teal sky"></div>
    <h1 class="title">
      <span class="title-line title-line--lead">Walk</span>
      <span class="title-line">Along</span>
      <span class="title-line">The</span>
      <span class="title-line">Harbor</span>
    </h1>
    <p class="artist">Dale Fennimore</p>
  </main>
</body>
</html>
```